Italian restaurant needs a flyer to promote wine tasting and wine pairing tours

Need a designer to create one flyer for print and digital use.

(3 pages all either postcard or 1/3 page)Intro page, wine tasting and wine pairing page, wine pairing and cruise page

We are Www.lunaverdetrattoria.com an top rated Italian restaurant in CABO San Lucas mexico. Our info and history is on the website. We are a fun, cozy bistro ambience that makes you feel like you are in Italy.

Get to know the great tastes of Rome right here in CABO San Lucas at Corvale Bistro. Farm and sea to table and select national and international wines . We begin with a brief introduction of the restaurant including a quick Salute to the kitchen then sit at our reserved table for a fun and tasty wine food pairing.

Our Founding Chef and In House Sommelier join forces to create four fabulous farm and sea to table dishes, using the freshest ingredients from local sources and only the top wines from small vineyards. Guests are guided through four wine & food pairings, with a some fun facts about wine and the wine producing regions of Mexico. A lively resort casual setting and a night you will never forget.

Wine & Dine Pairing Session includes:
* Welcome cocktail!
* 4-Course Wine Pairing menu
* Each course paired with local wines
* After Tasting Night cap
* Regional history, Wine tasting tips, trivia, and prizes!
* Guests receive 20% off their next reservation
* Everyday at 5:30pm and 9:30pm for one hour and 45 minutes.
* Limited to 10 guests per session please reserve in advance.
* 69usd X person. Tax included .

Target Market(s)

Wine lovers coming to CABO San Lucas

Industry/Entity Type

Restaurant

Font styles to use
Serif

Requirements
Must have
• More image and less text with an elegant yet fun setting
• Must have wine and dine description:
• Get to know the great tastes of Rome right here in CABO San Lucas at Corvale Bistro. Farm and sea to table and select national and international wines . We begin with a brief introduction of the restaurant including a quick Salute to the kitchen then sit at our reserved table for a fun and tasty wine food pairing.
• Our Founding Chef and In House Sommelier join forces to create four fabulous farm and sea to table dishes, using the freshest ingredients from local sources and only the top wines from small vineyards. Guests are guided through four wine & food pairings, with a some fun facts about wine and the wine producing regions of Mexico. A lively resort casual setting and a night you will never forget.
• Wine & Dine Pairing Session includes:
• * Welcome cocktail!
• * 4-Course Wine Pairing menu
• * Each course paired with local wines
• * After Tasting Night cap
• * Regional history, Wine tasting tips, trivia, and prizes!
• * Guests receive 20% off their next reservation
• * Everyday at 5:30pm and 9:30pm for one hour and 45 minutes.
• * Limited to 10 guests per session please reserve in advance.
• * 69usd X person. Tax included .
• amd must have wine tasting description:
• One hour of fun and flavor!
• Join our in house sommelier in this small group, one hour , lively happy hour party that includes ample tastes of 3 fine wines paired with authentic Italian gourmet appetizers and seasonal menu favorites. Let us share the best of Bajas wines amd perfectly paired tasting menu before hitting the town.
• This Wine Tasting Happy hour includes:
• * Welcome cocktail!
• * 4-Course Tasting menu
• * Each course paired with Baja local wines
• * Starts at 5pm or 6pm. Arrive 5 minutes prior for check in. Space is limited to 20 guests so advanced reservations are recommended.
• * 25usd per person tax included.
• Colors should be like our website www.lunaverdetrattoria.com
• Files must be editable
Nice to have
• Want this to focus on promoting the restaurant and tours
Should not have
• Errors

```html
<!DOCTYPE html>
<html lang="en">
<head>
<meta charset="utf-8">
<title>Corvale Bistro – Wine &amp; Dine Pairing</title>
<link rel="stylesheet" href="https://fonts.googleapis.com/css2?family=Cinzel:wght@400;600&family=Lato:wght@400&display=swap">
<style>
  :root {
    --canvas: #eceae6;
    --gold: #f2c21b;
    --gold-deep: #e3ac12;
    --gold-text: #f5cc2a;
    --ink: #1d1608;
    --night: #120c08;
    --cellar: #2a1a10;
    --wood: #7a4a24;
    --wine: #7c1414;
    --cream: #f3ead8;
  }
  * { margin: 0; padding: 0; box-sizing: border-box; }
  html, body { width: 1200px; height: 1200px; overflow: hidden; }
  body {
    background: var(--canvas);
    font-family: "Lato", sans-serif;
    display: flex; align-items: center; justify-content: center;
  }
  .brochure {
    display: flex;
    width: 1140px; height: 880px;
    box-shadow: 0 20px 50px rgba(0,0,0,.25);
  }
  .panel { position: relative; width: 380px; height: 880px; overflow: hidden; }

  /* Panel 1 – inclusions */
  .inclusions {
    height: 470px;
    background: radial-gradient(ellipse at 40% 30%, var(--gold) 0%, var(--gold-deep) 100%);
    padding: 70px 30px 0 36px;
    color: var(--ink);
  }
  .rule { height: 1px; background: var(--ink); opacity: .7; }
  .inclusions .rule.top { margin-left: 40px; margin-bottom: 26px; }
  .inclusions h2 {
    font-family: "Cinzel", serif; font-weight: 600;
    font-size: 14px; letter-spacing: .4px; margin-bottom: 12px;
  }
  .inclusions ul { padding-left: 16px; font-size: 12.5px; line-height: 1.42; }
  .inclusions li { margin-bottom: 1px; }
  .inclusions .rule.bottom { margin-top: 22px; }
  .photo-cellar-table {
    height: 410px;
    background: linear-gradient(160deg, #5a3620 0%, var(--wood) 45%, #3b2314 75%, #b88a5a 100%);
  }

  /* Panel 2 – reservations */
  .reservations {
    background: linear-gradient(180deg, var(--night) 0%, var(--cellar) 45%, #1b120c 80%, #3a2818 100%);
    color: var(--cream);
    display: flex; flex-direction: column; align-items: center;
    padding-top: 230px; text-align: center;
  }
  .brand-name {
    font-family: "Cinzel", serif; font-weight: 400;
    color: var(--gold-text); letter-spacing: 2px;
  }
  .brand-mark { display: flex; align-items: center; gap: 10px; }
  .brand-mark .dot { width: 10px; height: 10px; border-radius: 50%; background: var(--gold-text); }
  .reservations .brand-name { font-size: 26px; }
  .cuisine {
    font-family: "Cinzel", serif; color: var(--gold-text);
    font-size: 12px; letter-spacing: 1px;
    border-top: 1px solid var(--gold-text); border-bottom: 1px dashed var(--gold-text);
    padding: 6px 14px; margin-top: 14px;
  }
  .reserve-btn {
    margin-top: 40px; border: 2px solid var(--gold-text); color: var(--gold-text);
    font-family: "Cinzel", serif; font-weight: 600; font-size: 14px; letter-spacing: 1px;
    padding: 10px 14px;
  }
  .icon { width: 30px; height: 30px; margin-top: 22px; }
  .phone { font-family: "Cinzel", serif; font-size: 36px; color: #fff; margin-top: 6px; letter-spacing: 1px; }
  .address {
    font-family: "Cinzel", serif; font-size: 14px; color: #fff; line-height: 1.3; margin-top: 8px;
  }
  .web-block { position: absolute; bottom: 70px; left: 0; right: 0; text-align: center; }
  .web-block .rule { width: 200px; margin: 0 auto; background: var(--gold-text); }
  .web {
    font-family: "Cinzel", serif; color: #fff; font-size: 15px; letter-spacing: 3px;
    margin: 14px 0;
  }

  /* Panel 3 – cover */
  .cover { background: linear-gradient(180deg, #1a0f08 0%, #24160e 60%, #140c07 100%); }
  .photo-wine-pour {
    height: 480px;
    background: radial-gradient(circle at 35% 45%, #a4582a 0%, #6b3518 40%, #2a160b 80%);
  }
  .cover-brand { position: absolute; top: 550px; left: 0; right: 0; display: flex; flex-direction: column; align-items: center; }
  .cover .brand-name { font-size: 32px; }
  .cover .cuisine { font-size: 15px; }
</style>
</head>
<body>
<main class="brochure">
  <section class="panel panel-details">
    <div class="inclusions">
      <div class="rule top"></div>
      <h2>Wine &amp; Dine Pairing Session includes:</h2>
      <ul>
        <li>Welcome cocktail</li>
        <li>4-Course Wine Pairing menu</li>
        <li>Each course paired with local wines</li>
        <li>After Tasting Night cap</li>
        <li>Regional history, Wine tasting tips, trivia, and prizes!</li>
        <li>Guests receive 20% off their next reservation</li>
        <li>Everyday at 5:30pm and 9:30pm for one hour and 45 minutes.</li>
        <li>Limited to 10 guests per session please reserve in advance.</li>
        <li>69usd X person Tax included.</li>
      </ul>
      <div class="rule bottom"></div>
    </div>
    <div class="photo-cellar-table" role="img" aria-label="Photo of a wine bottle and a glass of red wine on a wooden table in front of a wine rack"></div>
  </section>

  <section class="panel reservations" role="img" aria-label="Dim photo of a wine cellar with bottles on shelves behind the text">
    <div class="brand-mark"><span class="dot"></span><span class="brand-name">Corvale Bistro</span></div>
    <div class="cuisine">Mediterranean Cuisine</div>
    <div class="reserve-btn">Reservation</div>
    <svg class="icon" viewBox="0 0 30 30" aria-hidden="true">
      <circle cx="15" cy="15" r="14" fill="var(--gold-text)"/>
      <path d="M10 8 l3 0 l1.5 4 l-2 1.5 a9 9 0 0 0 4 4 l1.5-2 l4 1.5 l0 3 a2 2 0 0 1-2 2 a14 14 0 0 1-12-12 a2 2 0 0 1 2-2z" fill="var(--night)"/>
    </svg>
    <div class="phone">148 2270</div>
    <svg class="icon" viewBox="0 0 30 30" aria-hidden="true">
      <circle cx="15" cy="15" r="14" fill="var(--gold-text)"/>
      <path d="M15 7 a5.5 5.5 0 0 1 5.5 5.5 c0 4-5.5 10-5.5 10 s-5.5-6-5.5-10 A5.5 5.5 0 0 1 15 7z" fill="var(--night)"/>
      <circle cx="15" cy="12.5" r="2" fill="var(--gold-text)"/>
    </svg>
    <div class="address">Av. Marina L-7, Centro<br>Cabo San Lucas, Mexico</div>
    <div class="web-block">
      <div class="rule"></div>
      <div class="web">www.lunaverdetrattoria.com</div>
      <div class="rule"></div>
    </div>
  </section>

  <section class="panel cover">
    <div class="photo-wine-pour" role="img" aria-label="Photo of red wine being poured into a glass in front of an oak barrel"></div>
    <div class="cover-brand">
      <div class="brand-mark"><span class="dot"></span><span class="brand-name">Corvale Bistro</span></div>
      <div class="cuisine">Mediterranean Cuisine</div>
    </div>
    <div class="web-block">
      <div class="rule"></div>
      <div class="web">www.lunaverdetrattoria.com</div>
      <div class="rule"></div>
    </div>
  </section>
</main>
</body>
</html>
```